Webdesign Hauskranken- und Tagespflege „Am Lindenhof“
Zielgruppe
Die Hauskranken- und Tagespflege „Am Lindenhof“ in Chemnitz ist ein unabhängiges, privat geführtes Unternehmen im Bereich der ambulanten und teilstationären Kranken- und Seniorenpflege. Seit der Gründung am 1. Mai 2007 stehen wir für eine zuverlässige, individuelle und herzliche Betreuung unserer Klientinnen und Klienten.
Das Team ist ein engagiertes Pflegeteam und auf über 35 qualifizierte Mitarbeiterinnen und Mitarbeiter angewachsen. Gemeinsam setzen wir uns täglich dafür ein, Menschen mit Pflegebedarf eine bestmögliche Versorgung und ein hohes Maß an Lebensqualität zu ermöglichen.
Unsere Firmenphilosophie basiert auf Wertschätzung, Vertrauen und Respekt – sowohl im Umgang mit unseren Klientinnen und Klienten sowie deren Angehörigen als auch innerhalb unseres Teams. Eine persönliche, einfühlsame und fachlich kompetente Betreuung steht für uns an erster Stelle.
Ob Grundpflege oder Behandlungspflege – bei uns sind Sie in guten Händen. Wir begleiten unsere Klientinnen und Klienten mit Fürsorge, Fachkompetenz und Herz und unterstützen sie dabei, ihren Alltag so selbstbestimmt wie möglich zu gestalten.
Gleichzeitig entlasten wir Angehörige, Freunde und Bekannte, indem wir ihnen Sicherheit geben und Freiräume schaffen. So bleibt mehr Zeit für gemeinsame, unbeschwerte Momente mit den Menschen, die ihnen am Herzen liegen.
Unsere Tagespflege bietet Platz für 18 Gäste. Der große Aufenthaltsraum mit offener Küche lädt zum gemütlichen Beisammensein ein. In unserem Ruheraum können sich unsere Gäste bei Bedarf zurückziehen und sich ausruhen, auch Therapien (Logopädie, Ergotherapie, Physiotherapie…) werden darin durchgeführt. Der Aufenthaltsraum ist zum Teil eingerichtet wie eine gemütliche Wohnstube, ihre Einrichtung erinnert an frühere Zeiten. Gemütliche Ruhesessel laden zum Entspannen ein.
Der persönliche Kontakt und das Vertrauen unserer Patientinnen und Patienten bilden dabei st..
Aufgabenstellung
Ziele des Relaunchs:
modernes, freundliches und barrierearmes Design
klare Benutzerführung für Senioren und Angehörige
Hinweis zum Rückrufservice
Notfallnummer dauerhaft sichtbar
schnelle Kontaktaufnahme (Telefon, Rückruf, Kontaktformular)
bessere Auffindbarkeit bei Google (SEO)
Vertrauen durch authentische Bilder, Teamvorstellung und Bewertungen

```html
<!DOCTYPE html>
<html lang="de">
<head>
<meta charset="utf-8">
<title>Webdesign-Konzept – Hauskranken- und Tagespflege „Am Lindenhof“</title>
<link href="https://fonts.googleapis.com/css2?family=Literata:ital,wght@0,400;0,500;0,600;1,400&family=Lexend:wght@300;400;500;600;700&display=swap" rel="stylesheet">
<style>
:root{
  --sun:#f3dc12;
  --navy:#1f2535;
  --paper:#fcf8ef;
  --ink:#2a2620;
  --silver:#c9ccd0;
  --line:#e6e0d2;
  --muted:#6b665d;
  --photo-a:#c9a98c;
  --photo-b:#8c7a66;
}
*{box-sizing:border-box;margin:0;padding:0}
html,body{width:1200px;height:3451px;overflow:hidden}
body{background:var(--paper);font-family:"Lexend",sans-serif;color:var(--ink);position:relative;font-size:10.5px;line-height:1.55}
.serif{font-family:"Literata",serif}
h1,h2,h3,h4{font-family:"Literata",serif;font-weight:500;color:var(--ink)}
.photo{background:linear-gradient(135deg,var(--photo-a),var(--photo-b));border-radius:4px}
.abs{position:absolute}

/* board header */
.board-head{position:absolute;left:0;top:0;width:1200px;height:98px;background:var(--navy);border-bottom:5px solid var(--sun);color:#fff}
.board-head .dot{position:absolute;left:46px;top:22px;width:48px;height:48px;border-radius:50%;background:var(--sun)}
.board-head .title{position:absolute;left:112px;top:26px;font-family:"Literata",serif;font-size:24px;font-weight:600}
.board-head .sub{position:absolute;left:112px;top:57px;font-size:10px;letter-spacing:2px;color:#b9bcc4}
.board-head .kind{position:absolute;right:44px;top:30px;font-size:12px;letter-spacing:3.5px;color:var(--sun);font-weight:600}
.board-head .scope{position:absolute;right:44px;top:54px;font-size:10.5px;letter-spacing:2px;color:#b9bcc4}
.label{position:absolute;font-size:11px;letter-spacing:2.6px;font-weight:600;color:#55514a}

/* desktop frame */
.desk{position:absolute;left:44px;top:139px;width:761px;height:3268px;background:var(--paper);border:1px solid var(--line);border-radius:8px 8px 0 0;overflow:hidden}
.browser{height:27px;background:#f3efe4;display:flex;align-items:center;padding-left:10px;gap:5px;border-bottom:1px solid var(--line)}
.browser i{width:8px;height:8px;border-radius:50%;display:block}
.browser .url{margin-left:14px;background:#fff;border-radius:4px;padding:1px 10px;font-size:10.5px;color:#555;width:520px}
.hotline{height:27px;background:var(--navy);color:#fff;display:flex;align-items:center;padding:0 99px;font-size:9.5px;gap:8px}
.hotline b{color:var(--sun);font-size:11.5px;font-weight:600;margin-left:6px}
.hotline .back{margin-left:auto;text-decoration:underline}
.nav{height:64px;display:flex;align-items:center;padding:0 99px;border-bottom:1px solid var(--line)}
.brand{display:flex;align-items:center;gap:10px}
.brand .dot{width:30px;height:30px;border-radius:50%;background:var(--sun)}
.brand span{font-family:"Literata",serif;font-size:11px;font-weight:600;line-height:1.2}
.nav ul{margin-left:auto;display:flex;gap:18px;list-style:none;font-size:10px;font-weight:600}
.wrap{padding:0 99px;position:relative}

.hero{height:333px;position:relative}
.hero h1{position:absolute;left:99px;top:34px;width:300px;font-size:31px;line-height:1.1}
.hero p{position:absolute;left:99px;top:146px;width:290px}
.btn{display:inline-flex;align-items:center;gap:6px;border-radius:6px;font-weight:600;font-size:11px}
.btn-sun{background:var(--sun);padding:10px 15px}
.btn-line{border:1.5px solid var(--ink);padding:8px 13px;font-size:10px}
.hero .b1{position:absolute;left:99px;top:231px}
.hero .b2{position:absolute;left:99px;top:278px}
.hero .photo{position:absolute;left:409px;top:70px;width:253px;height:201px}

.services{height:584px;position:relative;border-bottom:1px solid var(--line)}
.svc{position:absolute;top:24px;width:268px}
.svc .photo{height:167px}
.svc h3{font-size:15px;margin:12px 0 4px}
.svc ul{list-style:none;margin:12px 0 16px}
.svc li{position:relative;padding-left:13px;margin-bottom:9px;line-height:1.55}
.svc li::before{content:"";position:absolute;left:0;top:5px;width:6px;height:6px;border-radius:50%;background:var(--sun)}
.svc .note{border-top:1px solid var(--line);padding-top:12px}
.u{text-decoration:underline}

.day{height:456px;position:relative}
.day h2{position:absolute;left:99px;top:32px;font-size:20px;line-height:1.2}
.day dl{position:absolute;left:99px;top:106px;width:292px}
.day .row{display:flex;border-bottom:1px solid var(--line);padding:6px 0 9px;margin-bottom:6px}
.day .row:last-child{border:none}
.day dt{font-family:"Literata",serif;font-style:italic;width:88px;flex:none}
.day .ph{position:absolute;left:421px;width:242px}
.day .ph .photo{height:150px}
.day .ph p{font-size:8.5px;color:var(--muted);margin-top:5px;line-height:1.5}

.clock{height:273px;background:var(--navy);color:#fff;position:relative}
.clock h2{position:absolute;left:99px;top:38px;color:#fff;font-size:20px;line-height:1.2}
.clock p.lead{position:absolute;left:99px;top:98px;width:240px;color:#e5e6ea}
.clock .num{position:absolute;left:99px;top:180px;font-size:22px;color:var(--sun);font-weight:600}
.clock .hint{position:absolute;left:99px;top:224px;font-size:9px;color:#aeb2bb}
.clock svg{position:absolute;left:379px;top:70px}
.clock ul{position:absolute;left:528px;top:60px;list-style:none;width:140px}
.clock li{position:relative;padding-left:17px;margin-bottom:12px;font-size:9px;color:#aeb2bb;line-height:1.5}
.clock li b{display:block;color:#fff;font-size:10px;font-weight:600}
.clock li::before{content:"";position:absolute;left:0;top:3px;width:9px;height:9px;border-radius:50%}
.clock li.d1::before{background:var(--sun)}
.clock li.d2::before{background:#fff}
.clock li.d3::before{background:var(--silver)}

.faces{height:367px;position:relative}
.faces h2{position:absolute;left:99px;top:38px;font-size:20px}
.faces .intro{position:absolute;left:99px;top:77px;width:380px}
.team{position:absolute;left:99px;top:142px;display:flex;gap:88px}
.member{width:57px}
.member .photo{width:57px;height:70px}
.member h4{font-size:11px;font-weight:600;white-space:nowrap;margin-top:8px}
.member p{font-size:8.8px;color:var(--muted);width:125px;line-height:1.55}
.faces .outro{position:absolute;left:99px;top:303px;width:400px}

.voice{height:270px;position:relative;text-align:center;border-bottom:1px solid var(--line)}
.voice h2{padding-top:31px;font-size:17px}
.voice blockquote{font-family:"Literata",serif;font-style:italic;font-size:13.5px;line-height:1.55;margin-top:14px}
.voice cite{display:block;font-style:normal;font-size:9px;color:var(--muted);margin-top:10px}

.contact{height:652px;position:relative}
.contact h2{position:absolute;left:99px;top:40px;font-size:20px}
.form{position:absolute;left:99px;top:98px;width:287px;height:519px;background:#fff;border:1px solid var(--line);border-radius:6px;padding:18px 18px}
.form h3{font-size:13.5px}
.form .small{font-size:9px;color:var(--muted);margin-top:4px;line-height:1.5}
.form label{display:block;font-size:9.5px;font-weight:600;margin-top:12px}
.field{height:31px;border:1px solid #b9b3a5;border-radius:5px;background:#fbf8f1;margin-top:6px}
.field.big{height:62px}
.radios{display:flex;flex-wrap:wrap;gap:6px;margin-top:8px}
.radio{display:flex;align-items:center;gap:5px;border:1px solid #b9b3a5;border-radius:5px;padding:5px 7px;font-size:9.5px}
.radio.on{background:#f4eed9;border-color:var(--ink)}
.radio i{width:9px;height:9px;border-radius:50%;border:1px solid #777;display:block}
.radio.on i{background:radial-gradient(circle,#222 35%,#fff 40%)}
.check{display:flex;gap:8px;margin-top:14px;font-size:8.5px;color:var(--muted);line-height:1.55}
.check i{width:11px;height:11px;border:1px solid #888;flex:none;margin-top:2px}
.submit{margin-top:16px;background:var(--sun);border-radius:6px;text-align:center;padding:7px;font-weight:600;font-size:11px}
.form .alt{text-align:center;font-size:9px;color:var(--muted);margin-top:9px}
.addr{position:absolute;left:417px;top:94px;width:248px;font-size:9.5px}
.addr .r{display:flex;margin-bottom:6px}
.addr .r b{width:72px;flex:none;font-weight:600}
.house{position:absolute;left:417px;top:352px;width:245px;height:152px}
.house-cap{position:absolute;left:417px;top:510px;width:245px;font-size:8.5px;color:var(--muted)}

.foot{height:215px;background:var(--navy);color:#c9ccd3;position:relative;font-size:9px;line-height:1.55}
.foot h4{font-family:"Literata",serif;color:#fff;font-size:11px;font-weight:600;line-height:1.2}
.foot .c{position:absolute;top:30px}
.foot a{color:#fff;text-decoration:underline;display:block}
.foot .slogan{color:#fff;font-weight:600;font-size:9px}
.foot .copy{position:absolute;left:99px;top:188px;font-size:8px;color:#9ea2ab}

/* mobile */
.mob{position:absolute;left:896px;top:139px;width:208px;height:453px;background:var(--navy);border-radius:18px;padding:10px 10px 0;overflow:hidden}
.mob .scr{background:var(--paper);height:395px;border-radius:10px 10px 0 0;overflow:hidden;position:relative}
.mob .hl{background:var(--navy);color:#fff;font-size:8px;padding:9px 10px 5px;display:flex;gap:6px;align-items:center}
.mob .hl b{color:var(--sun);font-size:10px}
.mob .br{display:flex;gap:10px;align-items:center;padding:10px}
.mob .br .dot{width:22px;height:22px;border-radius:50%;background:var(--sun)}
.mob .br span{font-family:"Literata",serif;font-size:9.5px;font-weight:600;line-height:1.2}
.mob .mn{display:flex;flex-wrap:wrap;gap:8px 24px;font-size:8.5px;font-weight:600;padding:0 14px 10px;border-bottom:1px solid var(--line)}
.mob .photo{margin:16px 8px 0;height:103px}
.mob h2{font-size:18px;line-height:1.13;padding:20px 8px 0;width:140px}
.mob .bar{position:absolute;left:0;bottom:0;width:188px;height:48px;background:var(--navy);display:flex;gap:8px;padding:8px 6px}
.mob .bar div{border-radius:5px;font-size:8.5px;font-weight:600;display:flex;align-items:center;justify-content:center;gap:4px;height:26px}
.mob .bar .p{background:var(--sun);width:96px}
.mob .bar .r{border:1px solid #fff;color:#fff;flex:1}
.mob .home{position:absolute;left:76px;bottom:7px;width:56px;height:3px;background:#9aa0ab;border-radius:2px}

.detail{position:absolute;left:845px;top:1749px;width:310px;height:110px;background:var(--navy);border-radius:5px;color:#fff;overflow:hidden}
.detail h4{position:absolute;left:40px;top:14px;color:#fff;font-size:8px;line-height:1.15}
.detail p{position:absolute;left:40px;top:38px;width:100px;font-size:4.5px;line-height:1.5;color:#ccc}
.detail .n{position:absolute;left:40px;top:72px;font-size:8px;color:var(--sun);font-weight:600}
.detail svg{position:absolute;left:152px;top:28px}
.detail ul{position:absolute;left:216px;top:22px;list-style:none;width:60px;font-size:4px;line-height:1.4;color:#aaa}
.detail li{margin-bottom:5px}
.detail li b{color:#fff;display:block}

.concept{position:absolute;left:845px;top:2998px;width:310px;height:409px;background:#f6f0e2;border:1px solid var(--line);border-radius:6px;padding:18px 18px}
.concept h3{font-size:16px;margin-bottom:12px}
.concept h5{font-size:10.5px;font-weight:600;margin-top:10px}
.concept p{font-size:10.5px;line-height:1.5}
.sw{display:flex;gap:11px;margin-top:6px}
.sw div{text-align:center;font-size:7px;color:var(--muted)}
.sw i{display:block;width:44px;height:22px;border-radius:4px;margin-bottom:4px;border:1px solid var(--line)}
</style>
</head>
<body>

<header class="board-head">
  <div class="dot"></div>
  <div class="title">Hauskranken- und Tagespflege „Am Lindenhof“</div>
  <div class="sub">PFLEGE ZU HAUSE &amp; TAGESPFLEGE · CHEMNITZ</div>
  <div class="kind">WEBDESIGN-KONZEPT</div>
  <div class="scope">STARTSEITE · DESKTOP &amp; MOBILE</div>
</header>

<div class="label" style="left:46px;top:117px">DESKTOP · 1440 PX</div>
<div class="label" style="left:846px;top:117px">MOBILE · 390 PX</div>
<div class="label" style="left:846px;top:1731px">DETAIL · DIE 24-STUNDEN-UHR</div>

<main class="desk">
  <div class="browser"><i style="background:#e07b6a"></i><i style="background:#e6c25a"></i><i style="background:#8fbf72"></i><span class="url">hkp-am-lindenhof.de</span></div>
  <div class="hotline"><span>☾</span><span>24-Stunden-Hotline, auch nachts:</span><b>0371 / 48 220 60</b><span class="back">Oder wir rufen Sie zurück</span></div>
  <nav class="nav">
    <div class="brand"><div class="dot"></div><span>Hauskranken- und<br>Tagespflege<br>„Am Lindenhof“</span></div>
    <ul><li>Hauskrankenpflege</li><li>Tagespflege</li><li>Team</li><li>Kontakt</li></ul>
  </nav>

  <section class="hero">
    <h1>Zu Hause gut versorgt. Am Tag in guter Gesellschaft.</h1>
    <p>Seit dem 1. Mai 2007 pflegt und begleitet unser Team aus über 35 Mitarbeiterinnen und Mitarbeitern Menschen in Chemnitz: bei Ihnen zu Hause und in unserer Tagespflege an der Lindenallee.</p>
    <span class="btn btn-sun b1"><svg width="12" height="12" viewBox="0 0 24 24" fill="none" stroke="#222" stroke-width="2"><path d="M5 3h4l2 5-3 2a12 12 0 0 0 6 6l2-3 5 2v4a2 2 0 0 1-2 2A18 18 0 0 1 3 5a2 2 0 0 1 2-2z"/></svg>0371 / 48 220 60</span>
    <span class="btn btn-line b2">Wir rufen Sie zurück</span>
    <div class="photo" role="img" aria-label="Foto: lachende Pflegerin mit einer älteren Dame"></div>
  </section>

  <section class="services">
    <div class="svc" style="left:99px">
      <div class="photo" role="img" aria-label="Foto: Pflegerin hilft einer Seniorin im Wohnzimmer"></div>
      <h3>Hauskrankenpflege</h3>
      <p>Pflege und Hilfe in Ihrem Zuhause, damit Sie dort bleiben können, wo Sie sich auskennen.</p>
      <ul>
        <li><b>Grundpflege:</b> tägliche Körperpflege, Mahlzeiten, Unterstützung im Alltag</li>
        <li><b>Behandlungspflege:</b> Medikamente, Insulin, Injektionen und Wundversorgung nach ärztlicher Verordnung</li>
        <li><b>Hauswirtschaft:</b> Wäsche, Wohnung, Einkaufen, Begleitung zu Ärzten</li>
        <li><b>Kostenfreier Service:</b> Rezepte anfordern, Medikamente und Hilfsmittel nach Hause geliefert, Hilfe bei Anträgen</li>
      </ul>
      <p class="note">Wir kommen morgens, mittags oder abends, so wie es Ihre Pflege braucht. Und wir arbeiten eng mit Ihren Ärzten und Krankenkassen zusammen, damit Ihre Versorgung abgesichert ist.</p>
    </div>
    <div class="svc" style="left:393px">
      <div class="photo" role="img" aria-label="Foto: Gäste der Tagespflege beim gemeinsamen Spiel"></div>
      <h3>Tagespflege</h3>
      <p>Betreuung in geselliger Runde: Unsere Tagespflege bietet Platz für 18 Gäste.</p>
      <ul>
        <li><b>Geöffnet</b> Montag bis Freitag, 8 bis 16 Uhr, ein Tag oder die ganze Woche</li>
        <li><b>Fahrdienst</b> holt Sie morgens ab und bringt Sie nachmittags heim</li>
        <li><b>Wohnstube</b> mit offener Küche, Terrasse und gemütlichen Ruhesesseln</li>
        <li><b>Therapien im Haus:</b> Logopädie, Ergotherapie, Physiotherapie</li>
        <li><b>Barrierefrei</b>, mit Pflegebad und behindertengerechten Toiletten</li>
      </ul>
      <p class="note"><b>Aktuell sind Plätze frei.</b> Sabine Krause berät Sie gern unter <span class="u">0371 / 48 220 64</span>, Montag bis Freitag von 8 bis 14 Uhr. Bei Vorliegen eines Pflegegrades übernimmt Ihre Pflegekasse einen Großteil der Kosten.</p>
    </div>
  </section>

  <section class="day">
    <h2>So sieht ein<br>Tag bei uns aus</h2>
    <dl>
      <div class="row"><dt>Morgens</dt><dd>Der Fahrdienst holt Sie zu Hause ab. Angekommen, gibt es ein gemeinsames Frühstück.</dd></div>
      <div class="row"><dt>Am Vormittag</dt><dd>Zeitung lesen, Morgengymnastik, bei schönem Wetter ein Spaziergang oder die Terrasse. Es wird gemalt, gebastelt, gesungen, vorgelesen oder ein Kuchen gebacken.</dd></div>
      <div class="row"><dt>Mittags</dt><dd>Das Mittagessen kommt von einem regionalen Anbieter. Danach ist Zeit für ein Mittagsschläfchen in den Ruhesesseln.</dd></div>
      <div class="row"><dt>Am Nachmittag</dt><dd>Gemeinsames Kaffeetrinken und eine ruhige Plauderstunde zum Abschluss.</dd></div>
      <div class="row"><dt>Danach</dt><dd>Der Fahrdienst bringt Sie wieder nach Hause.</dd></div>
    </dl>
    <div class="ph" style="top:35px"><div class="photo" role="img" aria-label="Foto: Aufenthaltsraum mit offener Küche"></div><p>Echter Einblick: unser Aufenthaltsraum mit offener Küche.</p></div>
    <div class="ph" style="top:227px"><div class="photo" role="img" aria-label="Foto: Wohnstube mit Ruheecke"></div><p>Die Wohnstube mit Ruheecke, eingerichtet wie zu früheren Zeiten.</p></div>
  </section>

  <section class="clock">
    <h2>Wir sind rund um<br>die Uhr für Sie da.</h2>
    <p class="lead">Der Satz steht in unserem Logo, und er ist wörtlich gemeint: Tagsüber begleiten wir Sie zu Hause und in der Tagespflege. Nachts ist unsere Hotline besetzt.</p>
    <div class="num">0371 / 48 220 60</div>
    <div class="hint">Speichern Sie sich diese Nummer am besten gleich ein.</div>
    <svg width="120" height="120" viewBox="0 0 120 120">
      <circle cx="60" cy="60" r="55" fill="none" stroke="#f3dc12" stroke-width="5"/>
      <path d="M30 32 A40 40 0 0 1 90 32" fill="none" stroke="#c9ccd0" stroke-width="2"/>
      <circle cx="60" cy="5" r="5" fill="#f3dc12"/>
      <circle cx="60" cy="115" r="4" fill="#c9ccd0"/>
      <text x="60" y="38" font-family="Lexend,sans-serif" font-size="9" fill="#fff" text-anchor="middle">Mittag</text>
      <text x="60" y="98" font-family="Lexend,sans-serif" font-size="9" fill="#fff" text-anchor="middle">Mitternacht</text>
    </svg>
    <ul>
      <li class="d1"><b>24-Stunden-Hotline</b>Tag und Nacht erreichbar</li>
      <li class="d2"><b>Tagespflege</b>Montag bis Freitag, 8 bis 16 Uhr</li>
      <li class="d3"><b>Büro und Beratung</b>Montag bis Donnerstag 9 bis 15 Uhr, Freitag 9 bis 14 Uhr, und nach Vereinbarung</li>
    </ul>
  </section>

  <section class="faces">
    <h2>Bekannte Gesichter</h2>
    <p class="intro">Bezugspflege heißt für uns: feste Ansprechpartner, die Sie kennen und denen Sie vertrauen. Unser Pflegekonzept folgt dem Modell von Marianne Hollweg, aktivierend und fördernd.</p>
    <div class="team">
      <div class="member"><div class="photo" role="img" aria-label="Porträtfoto der Geschäftsführerin"></div><h4>Petra Lindner</h4><p>Geschäftsführerin, Pflegedienstleitung, examinierte Krankenschwester</p></div>
      <div class="member"><div class="photo" role="img" aria-label="Porträtfoto des Geschäftsführers"></div><h4>Jonas Lindner</h4><p>Geschäftsführer, 2. Pflegedienstleitung</p></div>
      <div class="member"><div class="photo" role="img" aria-label="Porträtfoto der Pflegedienstleitung"></div><h4>Karin Seidel</h4><p>1. Pflegedienstleitung, im Team seit 2014</p></div>
      <div class="member"><div class="photo" role="img" aria-label="Porträtfoto der Leitung Tagespflege"></div><h4>Sabine Krause</h4><p>Pflegedienstleitung Tagespflege, im Team seit 2011</p></div>
    </div>
    <p class="outro">Dahinter steht ein Team von über 35 Mitarbeiterinnen und Mitarbeitern in Pflege, Betreuung, Hauswirtschaft, Verwaltung und Fahrdienst.</p>
  </section>

  <section class="voice">
    <h2>Das sagen unsere Patienten</h2>
    <blockquote>„Da wohnt man gut im Lindenviertel,<br>weil’s dort ’ne feine Sache gibt:<br>die Hauskranken- und Tagespflege,<br>da ist man unermüdlich rege.<br>Schwestern und Pfleger sind dort täglich bereit,<br>helfen Patienten zu jeder Zeit. […]<br>Danke für die gute Pflege.“
      <cite>Aus einem Dankgedicht von Gisela und Werner Brandt an das Pflegeteam</cite></blockquote>
  </section>

  <section class="contact">
    <h2>So erreichen Sie uns</h2>
    <div class="form">
      <h3>Rückruf anfordern</h3>
      <p class="small">Hinterlassen Sie Ihre Nummer, wir rufen Sie werktags zurück.</p>
      <label>Ihr Name *</label><div class="field"></div>
      <label>Ihre Telefonnummer *</label><div class="field"></div>
      <label>Wann erreichen wir Sie am besten?</label>
      <div class="radios"><span class="radio on"><i></i>Am Vormittag</span><span class="radio"><i></i>Am Nachmittag</span><span class="radio"><i></i>Egal</span></div>
      <label>Ihre Nachricht (freiwillig)</label><div class="field big"></div>
      <div class="check"><i></i><span>Ich habe die <span class="u">Datenschutzerklärung</span> gelesen und bin einverstanden, dass meine Angaben zur Beantwortung meiner Anfrage gespeichert werden.</span></div>
      <div class="submit">Rückruf anfordern</div>
      <p class="alt">Oder rufen Sie direkt an: <b class="u">0371 / 48 220 60</b></p>
    </div>
    <div class="addr">
      <div class="r"><b>Adresse</b><span>Hauskranken- und Tagespflege „Am Lindenhof“<br>Lindenallee 27, 09130 Chemnitz</span></div>
      <div class="r"><b>Telefon</b><span><span class="u">0371 / 48 220 60</span> (24-Stunden-Hotline)</span></div>
      <div class="r"><b>Tagespflege</b><span class="u">0371 / 48 220 64</span></div>
      <div class="r"><b>Telefax</b><span>0371 / 48 220 66</span></div>
      <div class="r"><b>E-Mail</b><span class="u">info@hkp-am-lindenhof.de</span></div>
      <div class="r"><b>Bürozeiten</b><span>Montag bis Donnerstag 9 bis 15 Uhr, Freitag 9 bis 14 Uhr, und nach Vereinbarung</span></div>
    </div>
    <div class="photo house" role="img" aria-label="Foto: Eingang des Hauses an der Lindenallee mit gelben Fensterschildern"></div>
    <p class="house-cap">Unser Haus an der Lindenallee 27: Sie erkennen uns an der gelben Sonne.</p>
  </section>

  <footer class="foot">
    <div class="c" style="left:99px;width:190px"><h4>Hauskranken- und<br>Tagespflege „Am Lindenhof“</h4><div class="slogan">Wir sind rund um die Uhr für Sie da.</div>Lindenallee 27, 09130 Chemnitz<br>Telefon <span class="u">0371 / 48 220 60</span><a>info@hkp-am-lindenhof.de</a></div>
    <div class="c" style="left:329px"><h4>Rechtliches</h4><a style="margin-top:6px">Kontakt</a><a style="margin-top:8px">Datenschutz</a><a style="margin-top:8px">Impressum</a><a style="margin-top:8px">Erklärung zur Barrierefreiheit</a></div>
    <div class="c" style="left:489px;width:175px"><h4>Mitarbeit und Partner</h4><span class="slogan">Helft denen, die Hilfe brauchen.</span> Wir suchen Mitarbeiterinnen und Mitarbeiter für Pflege und Betreuung: <span class="u" style="color:#fff">0371 / 48 220 60</span><br>Wir arbeiten eng mit Ihren Hausärzten, Apotheken, Sanitätshäusern und Krankenkassen zusammen.</div>
    <div class="copy">© 2026 Hauskranken- und Tagespflege „Am Lindenhof“, Chemnitz</div>
  </footer>
</main>

<aside class="mob">
  <div class="scr">
    <div class="hl"><span>☾</span>24h-Hotline: <b>0371 / 48 220 60</b></div>
    <div class="br"><div class="dot"></div><span>Hauskranken- und<br>Tagespflege<br>„Am Lindenhof“</span></div>
    <div class="mn"><span>Hauskrankenpflege</span><span>Tagespflege</span><span>Team</span><span>Kontakt</span></div>
    <div class="photo" role="img" aria-label="Foto: lachende Pflegerin mit einer älteren Dame"></div>
    <h2>Zu Hause gut versorgt. Am Tag in guter Gesellschaft.</h2>
    <div class="bar"><div class="p">☏ 0371 / 48 220 60</div><div class="r">Rückruf</div></div>
  </div>
  <div class="home"></div>
</aside>

<div class="detail">
  <h4>Wir sind rund um<br>die Uhr für Sie da.</h4>
  <p>Der Satz steht in unserem Logo, und er ist wörtlich gemeint: Tagsüber begleiten wir Sie zu Hause und in der Tagespflege. Nachts ist unsere Hotline besetzt.</p>
  <div class="n">0371 / 48 220 60</div>
  <svg width="48" height="48" viewBox="0 0 120 120"><circle cx="60" cy="60" r="55" fill="none" stroke="#f3dc12" stroke-width="6"/><path d="M30 32 A40 40 0 0 1 90 32" fill="none" stroke="#c9ccd0" stroke-width="3"/><circle cx="60" cy="5" r="6" fill="#f3dc12"/></svg>
  <ul><li><b>24-Stunden-Hotline</b>Tag und Nacht erreichbar</li><li><b>Tagespflege</b>Montag bis Freitag, 8 bis 16 Uhr</li><li><b>Büro und Beratung</b>Montag bis Freitag, nach Vereinbarung</li></ul>
</div>

<aside class="concept">
  <h3>Das Konzept in Kürze</h3>
  <h5>Die Idee</h5>
  <p>Sonne und Mond aus dem Logo werden zur 24-Stunden-Uhr. Die Notfallnummer bleibt auf jedem Gerät sichtbar: oben als Leiste, unten als Anrufknopf.</p>
  <h5>Farben</h5>
  <div class="sw">
    <div><i style="background:var(--sun)"></i>Sonnengelb</div>
    <div><i style="background:var(--navy)"></i>Nachtblau</div>
    <div><i style="background:var(--paper)"></i>Papier</div>
    <div><i style="background:var(--ink)"></i>Tinte</div>
    <div><i style="background:var(--silver)"></i>Silber</div>
  </div>
  <h5>Schrift</h5>
  <p>Literata für Überschriften, eine warme Buchschrift. Lexend für den Fließtext, entworfen für leichteres Lesen.</p>
  <h5>Barrierearm</h5>
  <p>Schrift ab 18 px, hohe Kontraste, große Tasten, sichtbarer Fokus, keine versteckten Menüs, klare Sprache.</p>
  <h5>Vertrauen</h5>
  <p>Echte Fotos der Räume, das echte Team, ein echtes Dankgedicht von Patienten.</p>
</aside>

</body>
</html>
```